App-Design für IT-Sicherheitsfirma
Zielgruppe
Wir sind eine IT-Sicherheitsfirma und suchen ein funktionelles und schlankes App Design.
Unsere Nutzer sind Mitarbeiter von international agierenden Konzernen. Die Zielgruppe sind international agierende Konzerne.
Die App gibt die Möglichkeit zu einem sehr sicheren Login auf Großrechner (Mainframes) via Handy oder Webinterface. Vereinfacht gesagt ist sie ein Login-Tool, Schlüssel oder Authenticator.
Aufgabenstellung
Die App soll übersichtlich, sicher, modern, schlicht und smart aussehen. Schön aber kein muss wäre die Verwendung von Elementen aus 'wirbel/gestalt' da wir die App auf dieser Plattform programmieren wollen.
https://gestaltkern.io/design/gestalt-theming/overview.html#gestalt-theming
https://wirbel.dev/docs/development/ui/widgets/gestalt

```html
<!DOCTYPE html>
<html lang="en">
<head>
<meta charset="utf-8">
<title>Envoy pass – app screens</title>
<link href="https://fonts.googleapis.com/css2?family=Inter:wght@400;500;600;700&family=IBM+Plex+Mono:wght@400&display=swap" rel="stylesheet">
<style>
:root{
  --canvas:#e5e5e5;
  --screen:#f5f5f5;
  --surface:#ffffff;
  --ink:#111111;
  --ink-soft:#555555;
  --ink-mute:#777777;
  --line:#dddddd;
  --brand:#be2d24;
  --chip-grey:#e8e8e8;
  --chip-teal:#dcefee;
  --chip-rose:#f8e3e2;
}
*{box-sizing:border-box;margin:0;padding:0}
html,body{width:972px;height:1200px;overflow:hidden;background:var(--canvas);font-family:"Inter",sans-serif;color:var(--ink)}
.caption{position:absolute;left:133px;top:88px;font:7.5px/11px "IBM Plex Mono",monospace;color:#333}
.screen{position:absolute;width:200px;height:432px;background:var(--screen);overflow:hidden;box-shadow:0 6px 14px rgba(0,0,0,.08)}
.screen>*{position:absolute}
.backdrop{left:0;top:0;width:200px;height:432px;background:linear-gradient(160deg,#dcdbdb 0%,#e6e5e5 40%,#efefef 100%)}
.backdrop.short{height:230px}
.statusbar{left:0;top:0;width:200px;height:24px}
.statusbar .time{position:absolute;left:17px;top:7px;font-size:8px;font-weight:600}
.statusbar svg{position:absolute;right:9px;top:8px}
.app-title{left:0;width:200px;text-align:center;color:var(--brand);font-weight:600;font-size:17px;letter-spacing:-.1px}
.byline{left:0;width:200px;text-align:center;font-size:7.3px}
.sheet{left:0;width:200px;bottom:0;background:var(--screen);border-radius:10px 10px 0 0}
.field{left:13px;width:173px;height:33px;border:1px solid #333;background:var(--surface);padding:5px 5px 0}
.field.error{border-color:var(--brand)}
.field .label{font-size:7.3px;color:var(--ink-soft)}
.field .value{font-size:9.5px;font-weight:600;margin-top:2px;white-space:nowrap}
.error-text{left:13px;font-size:7.3px;color:var(--brand);display:flex;align-items:center;gap:3px}
.button{left:13px;width:173px;height:28px;background:var(--brand);color:#fff;font-size:9.5px;font-weight:600;display:flex;align-items:center;justify-content:center}
.device-note{left:0;width:200px;text-align:center;font-size:7.3px;line-height:9px;color:var(--ink-soft)}
.home-bar{left:64px;width:71px;height:2px;border-radius:1px;background:#111;top:426px}
.link{left:0;width:200px;text-align:center;font-size:7.3px;font-weight:600;color:var(--brand)}
.device-card{left:13px;top:246px;width:173px;height:56px;background:var(--surface);box-shadow:0 1px 3px rgba(0,0,0,.08)}
.device-card svg{position:absolute;left:13px;top:10px}
.device-card .name{position:absolute;left:45px;top:12px;font-size:9.5px;font-weight:600}
.device-card .meta{position:absolute;left:45px;top:25px;font-size:7.3px;line-height:9px;color:var(--ink-soft)}
.app-header{left:0;top:24px;width:200px;height:29px;background:var(--surface);border-bottom:1px solid var(--line)}
.app-header .h-title{position:absolute;left:13px;top:8px;font-size:11.5px;font-weight:600;color:#333}
.app-header .more{position:absolute;right:15px;top:8px;font-size:10px;letter-spacing:1px;color:#333}
.section-title{left:13px;top:85px;font-size:9px;color:var(--ink-soft)}
.filter{right:13px;top:86px;font-size:7.3px;font-weight:600;color:var(--brand)}
.mainframe{left:13px;width:173px;height:59px;background:var(--surface);box-shadow:0 1px 3px rgba(0,0,0,.08)}
.mainframe .drive{position:absolute;left:10px;top:14px}
.mainframe .name{position:absolute;left:45px;top:11px;font-size:9.5px;font-weight:600}
.mainframe .tag{position:absolute;left:45px;top:25px;display:flex;line-height:10px}
.mainframe .host{position:absolute;left:45px;top:40px;font-size:7.5px;color:var(--ink-soft)}
.mainframe .enter{position:absolute;right:8px;top:12px}
.chip{font:7px/10px "IBM Plex Mono",monospace;padding:0 3px;border-radius:2px;background:var(--chip-grey);display:inline-block}
.chip.teal{background:var(--chip-teal)}
.chip.rose{background:var(--chip-rose)}
.requests{left:0;top:99px;width:200px;background:var(--surface);border-top:1px solid var(--line)}
.request{position:relative;height:50px;border-bottom:1px solid var(--line)}
.request .check{position:absolute;left:13px;top:6px}
.request .name{position:absolute;left:34px;top:6px;font-size:9.5px;font-weight:600}
.request .date{position:absolute;left:34px;top:19px;font-size:7.5px;color:var(--ink-soft)}
.request .chips{position:absolute;left:34px;top:32px;display:flex;gap:3px}
.request .chev{position:absolute;right:10px;top:9px}
.tabbar{left:0;top:377px;width:200px;height:55px;background:var(--surface);border-top:1px solid var(--line)}
.tab{position:absolute;top:8px;width:80px;text-align:center;font-size:8.5px;color:var(--ink-mute)}
.tab.active{color:var(--brand)}
.tab svg{display:block;margin:0 auto 3px}
</style>
</head>
<body>

<div class="caption">Envoy pass<br>for veltrix</div>

<!-- Splash -->
<section class="screen" style="left:133px;top:133px">
  <div class="backdrop" role="img" aria-label="Soft grey low-poly background"></div>
  <div class="statusbar"><span class="time">9:41</span>
    <svg width="36" height="6" viewBox="0 0 36 6"><rect x="0" y="4" width="1.5" height="2" fill="#111"/><rect x="2.5" y="3" width="1.5" height="3" fill="#111"/><rect x="5" y="1.5" width="1.5" height="4.5" fill="#111"/><rect x="7.5" y="0" width="1.5" height="6" fill="#111"/><path d="M13 2.5a5 5 0 0 1 7 0M14.5 4a3 3 0 0 1 4 0" stroke="#111" stroke-width="1" fill="none"/><rect x="24" y="0.5" width="10" height="5" rx="1" fill="#111"/></svg>
  </div>
  <div class="app-title" style="top:212px">Envoy pass</div>
  <div class="byline" style="top:244px">by Veltrix</div>
</section>

<!-- Register -->
<section class="screen" style="left:386px;top:133px">
  <div class="backdrop short" role="img" aria-label="Soft grey low-poly background"></div>
  <div class="statusbar"><span class="time">9:41</span>
    <svg width="36" height="6" viewBox="0 0 36 6"><rect x="0" y="4" width="1.5" height="2" fill="#111"/><rect x="2.5" y="3" width="1.5" height="3" fill="#111"/><rect x="5" y="1.5" width="1.5" height="4.5" fill="#111"/><rect x="7.5" y="0" width="1.5" height="6" fill="#111"/><path d="M13 2.5a5 5 0 0 1 7 0M14.5 4a3 3 0 0 1 4 0" stroke="#111" stroke-width="1" fill="none"/><rect x="24" y="0.5" width="10" height="5" rx="1" fill="#111"/></svg>
  </div>
  <div class="app-title" style="top:113px">Envoy pass</div>
  <div class="sheet" style="top:160px"></div>
  <div class="field" style="top:186px"><div class="label">E-Mail</div><div class="value">lukas.brenner@veltrix.com</div></div>
  <div class="field" style="top:228px"><div class="label">First name</div><div class="value">Lukas</div></div>
  <div class="field" style="top:269px"><div class="label">Last name</div><div class="value">Brenner</div></div>
  <div class="button" style="top:310px">Register →</div>
  <div class="device-note" style="top:350px">Lukas' Phone<br>Lumo 12 Pro, LumoOS 14.6</div>
  <div class="home-bar"></div>
</section>

<!-- Register error -->
<section class="screen" style="left:639px;top:133px">
  <div class="backdrop short" role="img" aria-label="Soft grey low-poly background"></div>
  <div class="statusbar"><span class="time">9:41</span>
    <svg width="36" height="6" viewBox="0 0 36 6"><rect x="0" y="4" width="1.5" height="2" fill="#111"/><rect x="2.5" y="3" width="1.5" height="3" fill="#111"/><rect x="5" y="1.5" width="1.5" height="4.5" fill="#111"/><rect x="7.5" y="0" width="1.5" height="6" fill="#111"/><path d="M13 2.5a5 5 0 0 1 7 0M14.5 4a3 3 0 0 1 4 0" stroke="#111" stroke-width="1" fill="none"/><rect x="24" y="0.5" width="10" height="5" rx="1" fill="#111"/></svg>
  </div>
  <div class="app-title" style="top:113px">Envoy pass</div>
  <div class="sheet" style="top:160px"></div>
  <div class="field error" style="top:186px"><div class="label">E-Mail</div><div class="value">lukas.brenner@postmail.example</div></div>
  <div class="error-text" style="top:222px"><svg width="9" height="8" viewBox="0 0 9 8"><path d="M4.5 0.6L8.4 7.4H0.6Z" fill="none" stroke="#be2d24" stroke-width=".8"/><path d="M4.5 3v2M4.5 5.8v.6" stroke="#be2d24" stroke-width=".8"/></svg>This email is not allowed.</div>
  <div class="field" style="top:241px"><div class="label">First name</div><div class="value">Lukas</div></div>
  <div class="field" style="top:282px"><div class="label">Last name</div><div class="value">Brenner</div></div>
  <div class="button" style="top:323px">Register →</div>
  <div class="device-note" style="top:363px">Lukas' Phone<br>Lumo 12 Pro, LumoOS 14.6</div>
  <div class="home-bar"></div>
</section>

<!-- Login -->
<section class="screen" style="left:133px;top:646px">
  <div class="backdrop" role="img" aria-label="Soft grey low-poly background"></div>
  <div class="statusbar"><span class="time">9:41</span>
    <svg width="36" height="6" viewBox="0 0 36 6"><rect x="0" y="4" width="1.5" height="2" fill="#111"/><rect x="2.5" y="3" width="1.5" height="3" fill="#111"/><rect x="5" y="1.5" width="1.5" height="4.5" fill="#111"/><rect x="7.5" y="0" width="1.5" height="6" fill="#111"/><path d="M13 2.5a5 5 0 0 1 7 0M14.5 4a3 3 0 0 1 4 0" stroke="#111" stroke-width="1" fill="none"/><rect x="24" y="0.5" width="10" height="5" rx="1" fill="#111"/></svg>
  </div>
  <div class="app-title" style="top:172px">Envoy pass</div>
  <div class="sheet" style="top:219px"></div>
  <div class="device-card">
    <svg width="19" height="35" viewBox="0 0 19 35"><rect x="0.6" y="0.6" width="17.8" height="33.8" rx="1" fill="none" stroke="#111" stroke-width="1.1"/><path d="M7.5 31h4" stroke="#111" stroke-width="1"/></svg>
    <div class="name">Lukas' Phone</div>
    <div class="meta">Model: Lumo 12 Pro<br>OS: LumoOS 14.6</div>
  </div>
  <div class="button" style="top:310px">Login →</div>
  <div class="link" style="top:359px">Change account</div>
  <div class="home-bar"></div>
</section>

<!-- Terminal -->
<section class="screen" style="left:386px;top:646px">
  <div class="statusbar" style="background:var(--surface)"><span class="time">9:41</span>
    <svg width="36" height="6" viewBox="0 0 36 6"><rect x="0" y="4" width="1.5" height="2" fill="#111"/><rect x="2.5" y="3" width="1.5" height="3" fill="#111"/><rect x="5" y="1.5" width="1.5" height="4.5" fill="#111"/><rect x="7.5" y="0" width="1.5" height="6" fill="#111"/><path d="M13 2.5a5 5 0 0 1 7 0M14.5 4a3 3 0 0 1 4 0" stroke="#111" stroke-width="1" fill="none"/><rect x="24" y="0.5" width="10" height="5" rx="1" fill="#111"/></svg>
  </div>
  <header class="app-header"><span class="h-title">Envoy pass</span><span class="more">•••</span></header>
  <div class="section-title">Available mainframes</div>

  <div class="mainframe" style="top:99px">
    <svg class="drive" width="26" height="27" viewBox="0 0 26 27"><path d="M4 1h18l3 15v10H1V16Z M1 16h24" fill="none" stroke="#111" stroke-width="1.1"/><circle cx="20" cy="21" r="1.6" fill="none" stroke="#111" stroke-width="1"/></svg>
    <div class="name">Veltrix Demo</div>
    <div class="tag"><span class="chip">vts</span></div>
    <div class="host">mainframe.dev-veltrix.com</div>
    <svg class="enter" width="10" height="12" viewBox="0 0 10 12"><path d="M3 3V1h6v10H3V9M0 6h6M4 4l2 2-2 2" fill="none" stroke="#111" stroke-width="1"/></svg>
  </div>
  <div class="mainframe" style="top:166px">
    <svg class="drive" width="26" height="27" viewBox="0 0 26 27"><path d="M4 1h18l3 15v10H1V16Z M1 16h24" fill="none" stroke="#111" stroke-width="1.1"/><circle cx="20" cy="21" r="1.6" fill="none" stroke="#111" stroke-width="1"/></svg>
    <div class="name">Veltrix Test</div>
    <div class="tag"><span class="chip">vgrd</span></div>
    <div class="host">mainframe.dev-veltrix.com</div>
    <svg class="enter" width="10" height="12" viewBox="0 0 10 12"><path d="M3 3V1h6v10H3V9M0 6h6M4 4l2 2-2 2" fill="none" stroke="#111" stroke-width="1"/></svg>
  </div>
  <div class="mainframe" style="top:233px">
    <svg class="drive" width="26" height="27" viewBox="0 0 26 27"><path d="M4 1h18l3 15v10H1V16Z M1 16h24" fill="none" stroke="#111" stroke-width="1.1"/><circle cx="20" cy="21" r="1.6" fill="none" stroke="#111" stroke-width="1"/></svg>
    <div class="name">Veltrix Trial</div>
    <div class="tag"><span class="chip">virtual setup</span></div>
    <div class="host">mainframe.dev-veltrix.com</div>
    <svg class="enter" width="10" height="12" viewBox="0 0 10 12"><path d="M3 3V1h6v10H3V9M0 6h6M4 4l2 2-2 2" fill="none" stroke="#111" stroke-width="1"/></svg>
  </div>

  <nav class="tabbar">
    <div class="tab active" style="left:20px"><svg width="11" height="10" viewBox="0 0 11 10"><path d="M0 1h11M0 4h8M0 7h11M2 9.5h7" stroke="#be2d24" stroke-width="1"/></svg>Terminal</div>
    <div class="tab" style="left:100px"><svg width="12" height="11" viewBox="0 0 12 11"><path d="M2.2 3.2A4.8 4.8 0 1 1 1.5 6M0.8 1.5v2.4h2.4M6.5 3v3l2 1.2" fill="none" stroke="#777" stroke-width="1"/></svg>Logins</div>
  </nav>
  <div class="home-bar"></div>
</section>

<!-- Logins -->
<section class="screen" style="left:639px;top:646px">
  <div class="statusbar" style="background:var(--surface)"><span class="time">9:41</span>
    <svg width="36" height="6" viewBox="0 0 36 6"><rect x="0" y="4" width="1.5" height="2" fill="#111"/><rect x="2.5" y="3" width="1.5" height="3" fill="#111"/><rect x="5" y="1.5" width="1.5" height="4.5" fill="#111"/><rect x="7.5" y="0" width="1.5" height="6" fill="#111"/><path d="M13 2.5a5 5 0 0 1 7 0M14.5 4a3 3 0 0 1 4 0" stroke="#111" stroke-width="1" fill="none"/><rect x="24" y="0.5" width="10" height="5" rx="1" fill="#111"/></svg>
  </div>
  <header class="app-header"><span class="h-title">Envoy pass</span><span class="more">•••</span></header>
  <div class="section-title">Authentication requests</div>
  <div class="filter">Filter list</div>

  <div class="requests">
    <div class="request">
      <svg class="check" width="13" height="13" viewBox="0 0 13 13"><circle cx="6.5" cy="6.5" r="5.9" fill="none" stroke="#111" stroke-width="1"/><path d="M3.8 6.6l1.9 1.9 3.6-3.8" fill="none" stroke="#111" stroke-width="1"/></svg>
      <div class="name">Lukas Brenner</div>
      <div class="date">23.07.2021, 20:00:00</div>
      <div class="chips"><span class="chip teal">2FA</span><span class="chip rose">FingerID</span></div>
      <svg class="chev" width="6" height="9" viewBox="0 0 6 9"><path d="M1 1l3.5 3.5L1 8" fill="none" stroke="#111" stroke-width="1.1"/></svg>
    </div>
    <div class="request">
      <svg class="check" width="13" height="13" viewBox="0 0 13 13"><circle cx="6.5" cy="6.5" r="5.9" fill="none" stroke="#111" stroke-width="1"/><path d="M3.8 6.6l1.9 1.9 3.6-3.8" fill="none" stroke="#111" stroke-width="1"/></svg>
      <div class="name">Lukas Brenner</div>
      <div class="date">23.07.2021, 16:20:00</div>
      <div class="chips"><span class="chip teal">2FA</span><span class="chip rose">FingerID</span></div>
      <svg class="chev" width="6" height="9" viewBox="0 0 6 9"><path d="M1 1l3.5 3.5L1 8" fill="none" stroke="#111" stroke-width="1.1"/></svg>
    </div>
    <div class="request">
      <svg class="check" width="13" height="13" viewBox="0 0 13 13"><circle cx="6.5" cy="6.5" r="5.9" fill="none" stroke="#111" stroke-width="1"/><path d="M3.8 6.6l1.9 1.9 3.6-3.8" fill="none" stroke="#111" stroke-width="1"/></svg>
      <div class="name">Lukas Brenner</div>
      <div class="date">23.07.2021, 08:15:45</div>
      <div class="chips"><span class="chip">Accesstoken</span></div>
      <svg class="chev" width="6" height="9" viewBox="0 0 6 9"><path d="M1 1l3.5 3.5L1 8" fill="none" stroke="#111" stroke-width="1.1"/></svg>
    </div>
    <div class="request">
      <svg class="check" width="13" height="13" viewBox="0 0 13 13"><circle cx="6.5" cy="6.5" r="5.9" fill="none" stroke="#111" stroke-width="1"/><path d="M3.8 6.6l1.9 1.9 3.6-3.8" fill="none" stroke="#111" stroke-width="1"/></svg>
      <div class="name">Lukas Brenner</div>
      <div class="date">Yesterday, 23.07.2021, 23:52:56</div>
      <div class="chips"><span class="chip teal">2FA</span><span class="chip rose">FingerID</span></div>
      <svg class="chev" width="6" height="9" viewBox="0 0 6 9"><path d="M1 1l3.5 3.5L1 8" fill="none" stroke="#111" stroke-width="1.1"/></svg>
    </div>
  </div>

  <nav class="tabbar">
    <div class="tab" style="left:20px"><svg width="11" height="10" viewBox="0 0 11 10"><path d="M0 1h11M0 4h8M0 7h11M2 9.5h7" stroke="#777" stroke-width="1"/></svg>Terminal</div>
    <div class="tab active" style="left:100px"><svg width="12" height="11" viewBox="0 0 12 11"><path d="M2.2 3.2A4.8 4.8 0 1 1 1.5 6M0.8 1.5v2.4h2.4M6.5 3v3l2 1.2" fill="none" stroke="#be2d24" stroke-width="1"/></svg>Logins</div>
  </nav>
  <div class="home-bar"></div>
</section>

</body>
</html>
```